Bespoke catering company needs a simple but effective kick ass website

I need a website for a bespoke catering company based in the west side of Melbourne called "plova" by Marcus Pellow, I used the words Food-Dining-Events on my business cards which i still want to maintain through out the site.
My main market is aimed towards, in-house dining experiences of restaurant quality, cocktail food, small weddings / engagements, small events.
I have a plova logo in yellow in Hoefler title font with a black background, so the website design would include yellow and black and still using the Hoefler Titling font.
I want the site map to have 5 drop down bars including Home, About Me, Gallery, Menu, Contact me. It needs to be easy to move around.
I want links to my Facebook page, instagram and twitter.
The site needs to be easy for myself to change on a regular basis due to changing seasonal menus and gallery pictures.
Updates
Hi,
I have just added loads of photos of my food into the brief and adjusted the preferences slightly. Can you please update your submissions using my photos?
Thanks,
Marcus
Target Market(s)
The target market is customers looking for quality ,restaurant style dining and cocktail food in their own home or for their private event.
Industry/Entity Type
Restaurant
Font styles to use
Other font styles liked:
- Hoefler Titling
Look and feel
Each slider illustrates characteristics of the customer's brand and the style your logo design should communicate.

```html
<!DOCTYPE html>
<html lang="en">
<head>
<meta charset="utf-8">
<title>plova — About Me</title>
<link rel="stylesheet" href="https://fonts.googleapis.com/css2?family=Bebas+Neue&family=Lobster&family=Nunito+Sans:wght@400;600&display=swap">
<style>
  :root {
    --yellow: #ffdc00;
    --black: #0d0d0d;
    --white: #ffffff;
    --ink: #1a1a1a;
    --wood-light: #c9c2b8;
    --wood-mid: #a69d92;
    --wood-warm: #d8c3a8;
    --leaf: #8aa06a;
  }
  * { margin: 0; padding: 0; box-sizing: border-box; }
  html, body {
    width: 1200px;
    height: 1175px;
    overflow: hidden;
    background: var(--white);
  }
  .page {
    position: relative;
    width: 1200px;
    height: 1175px;
    background: var(--white);
  }
  .column {
    position: absolute;
    left: 285px;
    top: 19px;
    width: 630px;
  }
  .main-nav {
    display: flex;
    gap: 3px;
    height: 24px;
  }
  .main-nav a {
    flex: 1;
    display: flex;
    align-items: center;
    justify-content: center;
    background: var(--black);
    color: var(--white);
    text-decoration: none;
    font-family: "Bebas Neue", sans-serif;
    font-size: 12px;
    letter-spacing: 0.5px;
  }
  .main-nav a.is-current {
    background: var(--yellow);
    color: var(--black);
  }
  .intro-title {
    margin-top: 64px;
    font-family: "Bebas Neue", sans-serif;
    font-weight: 400;
    font-size: 53px;
    line-height: 44px;
    color: var(--yellow);
    letter-spacing: -0.3px;
  }
  .photo-strip {
    display: flex;
    gap: 3px;
    margin-top: 40px;
    height: 155px;
  }
  .photo { height: 100%; }
  .photo--sweets {
    width: 212px;
    background: linear-gradient(135deg, var(--wood-light), var(--wood-mid) 60%, #8a6a50);
  }
  .photo--salad {
    width: 220px;
    background: linear-gradient(135deg, var(--wood-light), var(--wood-mid) 55%, var(--leaf));
  }
  .photo--salmon {
    width: 192px;
    background: linear-gradient(135deg, var(--wood-warm), #ece4da 55%, #e3a27a);
  }
  .gallery-link {
    display: block;
    text-align: right;
    margin-top: 8px;
    text-decoration: none;
    color: var(--black);
  }
  .gallery-link__hint {
    display: block;
    font-family: "Bebas Neue", sans-serif;
    font-size: 7px;
    letter-spacing: 0.6px;
    line-height: 8px;
  }
  .gallery-link__label {
    display: block;
    font-family: "Lobster", cursive;
    font-size: 24px;
    line-height: 26px;
  }
  .section-title {
    margin-top: 14px;
    font-family: "Bebas Neue", sans-serif;
    font-weight: 400;
    font-size: 53px;
    line-height: 50px;
    color: var(--yellow);
  }
  .body-copy {
    font-family: "Nunito Sans", sans-serif;
    font-size: 10.6px;
    line-height: 13.6px;
    color: var(--ink);
  }
  .lead-copy {
    width: 396px;
    margin-top: 16px;
  }
  .split {
    display: flex;
    gap: 8px;
    width: 396px;
    margin-top: 2px;
  }
  .pull-quote {
    width: 128px;
    flex: none;
    margin-top: 10px;
    font-family: "Lobster", cursive;
    font-size: 20.5px;
    line-height: 24px;
    color: var(--black);
  }
  .split .body-copy { flex: 1; }
</style>
</head>
<body>
<main class="page">
  <div class="column">
    <nav class="main-nav">
      <a href="#">Home</a>
      <a href="#" class="is-current">About Me</a>
      <a href="#">Menu</a>
      <a href="#">Gallery</a>
      <a href="#">Contact Me</a>
    </nav>

    <h1 class="intro-title">A bespoke home-catering company<br>located in the west side of<br>Melbourne.</h1>

    <div class="photo-strip">
      <div class="photo photo--sweets" role="img" aria-label="Photo of meringue canapés on a wooden board"></div>
      <div class="photo photo--salad" role="img" aria-label="Photo of a green salad in a white bowl with servers"></div>
      <div class="photo photo--salmon" role="img" aria-label="Photo of salmon canapés on a white platter"></div>
    </div>

    <a href="#" class="gallery-link">
      <span class="gallery-link__hint">CLICK TO VIEW</span>
      <span class="gallery-link__label">Gallery</span>
    </a>

    <h2 class="section-title">Lorem ipsum dolor sit</h2>

    <p class="body-copy lead-copy">Sed felis enim, varius sit amet ante at, cursus pharetra tellus. Vestibulum ante ipsum primis in faucibus orci luctus et ultrices posuere cubilia Curae; Ut porttitor urna sodales augue ullamcorper feugiat. Praesent et laoreet turpis. Suspendisse malesuada massa vitae feugiat aliquam. Praesent euismod justo non lectus tincidunt bibendum. Cras convallis dapibus mi malesuada consequat. Morbi malesuada pulvinar sodales. Sed ullamcorper rutrum pulvinar. Morbi a diam sit amet nulla facilisis vulputate adipiscing non velit. Suspendisse sed velit erat. Aenean viverra molestie nisi, fermentum lobortis augue consequat id. Quisque eu enim non elit consectetur luctus. Vestibulum blandit turpis lacus, vulputate tincidunt sem accumsan ut. Vivamus ut egestas tortor.</p>

    <div class="split">
      <blockquote class="pull-quote">“Nam ultricies consequat odio ac tristique maecenas non augue eget dolor.”</blockquote>
      <p class="body-copy">Aliquam molestie sem sit amet orci vulputate, eget blandit est interdum. Ut et aliquet nulla. Mauris venenatis cursus lorem, vitae lacinia est sollicitudin eget. Sed luctus nisi eget risus ornare, sed auctor nunc dignissim. Cras varius aliquet odio nec viverra. Proin iaculis rutrum purus ac pharetra. Suspendisse condimentum volutpat elit. Nam ultricies consequat odio ac tristique. Maecenas non augue eget dolor posuere condimentum sed ultricies tortor. Maecenas aliquet nisi vel lectus.</p>
    </div>
  </div>
</main>
</body>
</html>
```